Crestline Gas and Plumbing Business Card Design

I am after a business card design for my plumbing business called 'Crestline Gas & Plumbing'. I do all types of plumbing and gas work and specialise in general maintenance plumbing. Would like to see designs using current logo

Industry/Entity Type

Plumbing

Contact Information for Business Card

Name - Dale Whitcombe
Phone number - 0455163027
Email - admin@crestlinegasandplumbing.example.com.au
ABN - 68204915336

```html
<!DOCTYPE html>
<html lang="en">
<head>
<meta charset="utf-8">
<title>Crestline Gas &amp; Plumbing – Business Card</title>
<link rel="stylesheet" href="https://fonts.googleapis.com/css2?family=Open+Sans:wght@400;600;700;800&display=swap">
<style>
  :root {
    --backdrop: #2b2b2d;
    --blue-deep: #1f2a9c;
    --blue-mid: #2c45c9;
    --blue-light: #3b6ee0;
    --orange: #f07b1c;
    --white: #ffffff;
    --logo-blue: #1e5fb3;
  }
  * { box-sizing: border-box; margin: 0; padding: 0; }
  html, body {
    width: 1200px; height: 960px; overflow: hidden;
    background: var(--backdrop);
    font-family: "Open Sans", Arial, sans-serif;
  }
  .stage {
    position: relative; width: 1200px; height: 960px;
  }
  .card {
    position: absolute; width: 580px; height: 350px;
    border-radius: 6px; overflow: hidden;
    box-shadow: 0 14px 32px rgba(0,0,0,0.45);
  }
  /* Back of card */
  .card-back {
    left: 310px; top: 95px;
    background: linear-gradient(160deg, var(--blue-deep) 0%, var(--blue-mid) 55%, var(--blue-light) 100%);
    display: flex; align-items: center; justify-content: center;
  }
  .card-back .wordmark {
    display: flex; align-items: center; gap: 14px;
    color: var(--white); font-weight: 800; font-size: 34px;
    letter-spacing: 0.5px;
  }
  .wordmark .mark-dot {
    width: 22px; height: 22px; border-radius: 50%;
    background: currentColor; flex: none;
  }
  /* Front of card */
  .card-front {
    left: 310px; top: 515px;
    background: var(--white);
  }
  .card-front .wordmark {
    position: absolute; left: 34px; top: 46px;
    display: flex; align-items: center; gap: 12px;
    color: var(--logo-blue); font-weight: 800; font-size: 28px;
    letter-spacing: 0.3px;
  }
  .card-front .holder-name {
    position: absolute; left: 34px; top: 160px;
    color: var(--orange); font-weight: 700; font-size: 30px;
    letter-spacing: 0.5px; text-transform: uppercase;
  }
  .contact-band {
    position: absolute; left: 0; bottom: 0; width: 100%; height: 128px;
    background: linear-gradient(90deg, var(--blue-deep) 0%, var(--blue-mid) 60%, var(--blue-light) 100%);
    padding: 22px 34px;
    color: var(--white); font-size: 15px; line-height: 27px;
  }
  .contact-line { display: flex; align-items: center; gap: 10px; }
  .contact-line svg { width: 15px; height: 15px; fill: var(--white); flex: none; }
  .contact-line .no-icon { width: 15px; flex: none; }
</style>
</head>
<body>
<main class="stage">
  <section class="card card-back" aria-label="Card back">
    <div class="wordmark"><span class="mark-dot"></span>Crestline Gas &amp; Plumbing</div>
  </section>

  <section class="card card-front" aria-label="Card front">
    <div class="wordmark"><span class="mark-dot"></span>Crestline Gas &amp; Plumbing</div>
    <h1 class="holder-name">Dale Whitcombe</h1>
    <div class="contact-band">
      <p class="contact-line">
        <svg viewBox="0 0 24 24" aria-hidden="true"><path d="M6.6 10.8a15.1 15.1 0 0 0 6.6 6.6l2.2-2.2a1 1 0 0 1 1-.25 11.4 11.4 0 0 0 3.6.57 1 1 0 0 1 1 1V20a1 1 0 0 1-1 1A17 17 0 0 1 3 4a1 1 0 0 1 1-1h3.5a1 1 0 0 1 1 1c0 1.25.2 2.45.57 3.57a1 1 0 0 1-.25 1z"/></svg>
        0455163027
      </p>
      <p class="contact-line">
        <svg viewBox="0 0 24 24" aria-hidden="true"><path d="M2 5h20v14H2z M3.5 6.5 12 12.5l8.5-6v-.1H3.5z" fill-rule="evenodd"/><path d="M3 6l9 6.5L21 6v1.6l-9 6.4-9-6.4z" fill="#2c45c9"/></svg>
        admin@crestlinegasandplumbing.example.com.au
      </p>
      <p class="contact-line"><span class="no-icon"></span>ABN 68204915336</p>
    </div>
  </section>
</main>
</body>
</html>
```